Creating a Label for a new CBD Vape Line call "Brisq".

This will be a project that will create the first label design on a BRISQ Vape product that is being rolled out in Colorado. The vape line will cater to high concentration CBD Vape sold in disposable vape pens and replacement cartridge's. In the sea of vape pens we want our packaging to stand out with a bold, bright, clean, abstract design that will highlight the brand "BRISQ" in a font that stands out and is quickly recognized. The target demographic for this line is 18-29 years of age. The mock up of the brisq vape picture does not meet our marketing desire, I just wanted to show you the approximate shape and size of the label and that the font used for the label will be added to the actual pen. This pen will have 100% CBD, cut with all natural terpenes with no need for chemicals like PG or VG, not many on the market like that. I included several marketing logos that caught our eye with other type product, please look at those as examples but we are open to creativity.

Target Market(s)

18-29 year old

Industry/Entity Type

CBD and Vape

Font styles to use
Serif
Sans Serif

Requirements
Must have
• bold, colorful, fun, eye catching
Nice to have
• Several brand ideas presented to give the flavor of the marketing. The example font on the prototype is not 'cool enough' to use, we'd like that name BRISQ to look and feel briiiisq. :-)
Should not have
• old school, boring, dull colors, small font

```html
<!DOCTYPE html>
<html lang="en">
<head>
<meta charset="utf-8">
<title>Brisq Vivo Vepe Label</title>
<link rel="stylesheet" href="https://fonts.googleapis.com/css2?family=Montserrat:ital,wght@0,700;0,800;1,800&family=Lato:wght@400&display=swap">
<style>
  :root {
    --page: #e9ebee;
    --label-deep: #04142a;
    --label-mid: #0a2c52;
    --smoke: #1d5f9c;
    --tab: #0f3f6b;
    --white: #ffffff;
    --age-blue: #1fa8f0;
    --brand-blue: #a9dcff;
  }
  * { margin: 0; padding: 0; box-sizing: border-box; }
  html, body { width: 802px; height: 1200px; overflow: hidden; background: var(--page); }
  .label {
    position: absolute;
    left: 21px; top: 422px;
    width: 760px; height: 355px;
    background: var(--label-deep);
    overflow: hidden;
    font-family: "Montserrat", sans-serif;
    color: var(--white);
  }
  .smoke-art {
    position: absolute; inset: 0;
    background:
      radial-gradient(ellipse 300px 140px at 370px 190px, rgba(60,140,220,0.55), transparent 70%),
      radial-gradient(ellipse 420px 220px at 380px 160px, var(--smoke), transparent 75%),
      linear-gradient(180deg, var(--label-mid), var(--label-deep));
    opacity: 0.85;
  }
  .product-tab {
    position: absolute;
    left: 179px; top: 0;
    width: 395px; height: 88px;
    background: var(--tab);
    border-radius: 0 0 26px 26px;
    display: flex; align-items: center; justify-content: center;
  }
  .product-name { font-weight: 800; font-size: 43px; letter-spacing: 0.5px; }
  .age-mark {
    position: absolute;
    left: 611px; top: 36px;
    font-weight: 800; font-style: italic;
    color: var(--age-blue);
    font-size: 30px;
  }
  .age-mark small { font-size: 19px; }
  .brand-name {
    position: absolute;
    left: 0; width: 740px; top: 120px;
    text-align: center;
    font-weight: 800;
    font-size: 112px;
    color: var(--brand-blue);
    letter-spacing: 2px;
  }
  .strength-tab {
    position: absolute;
    left: 186px; top: 287px;
    width: 384px; height: 54px;
    background: var(--tab);
    border-radius: 27px;
    display: flex; align-items: center; justify-content: center;
  }
  .strength { font-weight: 800; font-size: 36px; letter-spacing: 0.5px; }
  .disclaimer {
    position: absolute;
    left: 603px; top: 262px;
    width: 130px;
    font-family: "Lato", sans-serif;
    font-size: 10.5px; line-height: 1.3;
    text-align: center;
  }
</style>
</head>
<body>
  <section class="label">
    <div class="smoke-art" role="img" aria-label="Soft blue smoke drifting across a dark navy background"></div>
    <div class="product-tab"><span class="product-name">Vivo Vepe</span></div>
    <div class="age-mark">21<small>YRS</small>+</div>
    <div class="brand-name">Brisq</div>
    <div class="strength-tab"><span class="strength">450 MG CBD</span></div>
    <p class="disclaimer">These statements have not been evaluated by the food and drug administration. This Product is not intended to treat cure or prevent any disease</p>
  </section>
</body>
</html>
```